Wine Bottle Lable

Want a unique, simple but elegant, label for a wine bottle. I want to use the letters "DKP" in the design which is a moniker for my last name "Dufkamp". The letters DKP do not have to be juxtaposed together so that it is recognizable, or they could be something like D-KP, KP-D, DPK D-KP-D, etc. The X could be totally separated from the NO, or otherwise. The wine is a white wine in a clear bottle. I need Adobe Illustrator files so I can add the wine varietal, year, alcohol content. The label should be 4" wide and 5" tall.

Colors

Designer to choose colors to be used in the design.

Requirements
Nice to have
• outstanding but simple graphics

```html
<!DOCTYPE html>
<html lang="en">
<head>
<meta charset="utf-8">
<title>DKP White Wine Label</title>
<link rel="stylesheet" href="https://fonts.googleapis.com/css2?family=Marcellus&family=Oswald:wght@300&display=swap">
<style>
  :root {
    --page: #f4f4f5;
    --sky-top: #dcebfa;
    --sky-mid: #bfe0f7;
    --mint: #b9ecdc;
    --paper: #ffffff;
    --ribbon-shade: #e6e7ea;
    --gold: #c9a24a;
    --seal: #ececee;
    --ink-soft: #7d8287;
    --ink-dark: #3a3b3d;
  }
  html, body {
    margin: 0;
    padding: 0;
    width: 1200px;
    height: 1000px;
    overflow: hidden;
    background: var(--page);
  }
  .label {
    position: absolute;
    left: 240px;
    top: 50px;
    width: 720px;
    height: 900px;
    overflow: hidden;
    background: var(--paper);
    box-shadow: 0 2px 10px rgba(0,0,0,0.08);
  }
  .label-art {
    position: absolute;
    inset: 0;
    width: 720px;
    height: 900px;
  }
  .varietal-title {
    position: absolute;
    top: 165px;
    left: 0;
    width: 720px;
    text-align: center;
    margin: 0;
    font-family: "Marcellus", serif;
    font-weight: 400;
    font-size: 42px;
    letter-spacing: 1px;
    color: var(--ink-soft);
  }
  .brand-name {
    position: absolute;
    top: 408px;
    left: 0;
    width: 720px;
    text-align: center;
    margin: 0;
    font-family: "Marcellus", serif;
    font-size: 78px;
    letter-spacing: 4px;
    line-height: 82px;
    color: var(--ink-dark);
  }
  .vintage {
    position: absolute;
    top: 692px;
    left: 0;
    width: 720px;
    text-align: center;
    margin: 0;
    font-family: "Marcellus", serif;
    font-size: 26px;
    letter-spacing: 2px;
    color: var(--ink-soft);
  }
  .legal {
    position: absolute;
    left: 40px;
    top: 800px;
    margin: 0;
    font-family: "Oswald", sans-serif;
    font-weight: 300;
    font-size: 27px;
    line-height: 35px;
    color: var(--ink-dark);
  }
</style>
</head>
<body>
  <main class="label">
    <svg class="label-art" viewBox="0 0 720 900" xmlns="http://www.w3.org/2000/svg">
      <defs>
        <linearGradient id="wash" x1="0" y1="0" x2="0.3" y2="1">
          <stop offset="0" stop-color="var(--sky-top)"/>
          <stop offset="0.5" stop-color="var(--sky-mid)"/>
          <stop offset="1" stop-color="var(--mint)"/>
        </linearGradient>
        <linearGradient id="ribbon" x1="0" y1="0" x2="1" y2="1">
          <stop offset="0" stop-color="var(--paper)"/>
          <stop offset="1" stop-color="var(--ribbon-shade)"/>
        </linearGradient>
        <radialGradient id="pearl" cx="0.35" cy="0.3" r="0.75">
          <stop offset="0" stop-color="#ffffff"/>
          <stop offset="0.7" stop-color="#eeeff1"/>
          <stop offset="1" stop-color="#d3d5d8"/>
        </radialGradient>
      </defs>

      <rect class="watercolour-wash" role="img" aria-label="Soft sky blue to mint watercolour wash" width="720" height="900" fill="url(#wash)"/>

      <g class="corner-ribbon-top">
        <polygon points="0,0 165,0 0,500" fill="url(#ribbon)"/>
        <line x1="163" y1="0" x2="0" y2="495" stroke="var(--gold)" stroke-width="2.5"/>
        <line x1="108" y1="0" x2="0" y2="190" stroke="var(--gold)" stroke-width="2"/>
      </g>

      <g class="corner-ribbon-bottom">
        <polygon points="720,570 720,900 455,900" fill="url(#ribbon)"/>
        <line x1="720" y1="568" x2="452" y2="900" stroke="var(--gold)" stroke-width="2.5"/>
        <line x1="720" y1="810" x2="590" y2="900" stroke="var(--gold)" stroke-width="2"/>
      </g>

      <g class="pearls">
        <circle cx="190" cy="131" r="32" fill="url(#pearl)"/>
        <circle cx="633" cy="355" r="53" fill="url(#pearl)"/>
        <circle cx="117" cy="722" r="28" fill="url(#pearl)"/>
        <circle cx="581" cy="740" r="46" fill="url(#pearl)"/>
      </g>

      <circle class="seal-ornament" role="img" aria-label="Gold swirl wreath around the brand seal" cx="361" cy="449" r="220" fill="var(--seal)"/>
      <circle class="seal-ring" cx="361" cy="449" r="139" fill="none" stroke="var(--ink-dark)" stroke-width="8"/>
    </svg>

    <h1 class="varietal-title">WHITE WINE</h1>
    <p class="brand-name">DKP</p>
    <p class="vintage">2015</p>
    <p class="legal">WHITE WINE • VIN BLANC<br>11% ALC./VOL • 750mL</p>
  </main>
</body>
</html>
```